Website brand design for space sector startup

Amber Tide Orbital is a new company which specialises in the development of technologies for the space sector including propulsion systems, cubesat hardware and software, robotics hardware and software, rocket flight computers, miniature manufacturing units for space, scientific measurement equipment for space, guidance and communication systems amongst other more exotic technologies.

Amber Tide Limited, its parent company was originally founded to provide software development services with a heavy weighting towards .NET software for the web and desktop with some development services for the embedded sector.
This business is continuing to grow but over recent years the business has taken on more and more specialised projects which are heavily focused on the space sector. To avoid confusion for clients, Amber Tide Limited split out any non-software projects into a seperate department which included its own temporary independent website.
However, since all these projects are space related and since Amber Tide Limited is going through a rebrand and restructuring exercise, we've decided to formalise the space business more and to run two websites, Amber Tide Orbital which focusses on software and Amber Tide Orbital which focusses on space related projects.

This competition is for a new Amber Tide Orbital website which will focus on space related technologies and projects. A link to the previous temporary technology website can be provided if needed as well as to our current software website.
We may run a follow on competition for the software website if we feel that some re-alignment of brand is needed towards the new space website.
However, this competition is for the space related website and so we don't want the current websites to have too much influence over the new website.
We also plan to run follow on competitions for branded literature etc.
We have attached the new logo which will be edited to say Amber Tide Orbital and will be used for the new website.

The website should convey high tech creative, exciting space technologies, possibly including sats/cubesats, robotic rovers and rockets amongst other things.

Just to clarify, this design is for the space sector website, not the software website.

Target Market(s)

Companies operating in the space sector is of primary concern although it would be a benefit to also spark the interest of broader public

Industry/Entity Type

Communication

Requirements
Must have
• We would like to have a few pages which possibly show different images and/or backgrounds to make the site interesting to navigate.
Should not have
• Should not be a website for a software company but is for the space technology business and should focus more on space technology such as rockets, satellites, robotics/rovers or other space technologies and not boxed software.

```html
<!DOCTYPE html>
<html lang="en">
<head>
<meta charset="utf-8">
<title>Amber Tide Orbital</title>
<link rel="stylesheet" href="https://fonts.googleapis.com/css2?family=Open+Sans:wght@400;600&display=swap">
<style>
:root{
  --page:#000;
  --ink:#2a2a2a;
  --brand-red:#b0121a;
  --accent-orange:#e8541c;
  --cream:#f1dfae;
  --strip:#3a3a3a;
  --strip-dark:#2a1a17;
  --line:#c9c9c9;
  --date:#1e5ea8;
}
*{box-sizing:border-box;margin:0;padding:0}
html,body{width:1000px;height:1200px;overflow:hidden;background:var(--page)}
body{position:relative;font-family:"Open Sans",Arial,sans-serif;color:var(--ink)}
.abs{position:absolute}

/* header */
.site-header{left:20px;top:25px;width:960px;height:104px;background:linear-gradient(#fff,#ececec);border-bottom:6px solid #d8d8d8}
.brand{left:38px;top:34px;font-weight:600;font-size:32px;color:var(--brand-red);white-space:nowrap}
.search{left:770px;top:22px;width:164px;height:27px;border:2px solid #d2d2d2;border-radius:5px;background:#f2f2f2;font-size:16px;color:#b5b5b5;padding:2px 0 0 13px}
.search svg{position:absolute;right:8px;top:3px}
.main-nav{left:451px;top:65px;display:flex;font-size:13px;color:#666}
.main-nav a{color:inherit;text-decoration:none;display:block;height:28px;line-height:28px;white-space:nowrap}
.main-nav .current{width:80px;text-align:center;background:linear-gradient(#fff,#dcdcdc);border:1px solid #c8c8c8;border-bottom:none}
.main-nav .n2{margin-left:47px}.main-nav .n3{margin-left:55px}.main-nav .n4{margin-left:82px}

/* hero */
.hero{left:24px;top:138px;width:952px;height:296px;border-radius:6px;background:radial-gradient(circle at 60% 40%,#4a3a22 0%,#1e1710 45%,#0a0806 100%)}
.hero-rocket{left:110px;top:40px;width:160px;height:260px;border-radius:50%;background:radial-gradient(#8a8f99,#3a3c42 60%,transparent 72%);opacity:.7}
.hero-globe{left:680px;top:22px;width:168px;height:168px;border-radius:50%;background:radial-gradient(circle at 40% 35%,#7fa3c7,#2e4a6a 60%,#0e1622)}
.hero-tagline{left:391px;top:226px;width:480px;text-align:center;color:var(--accent-orange);font-size:20px;line-height:21px}

/* feature strip */
.features{left:28px;top:443px;width:944px;height:96px;border-radius:6px;background:var(--strip);overflow:hidden}
.features .first{left:0;top:0;width:300px;height:96px;background:linear-gradient(90deg,var(--strip-dark),#3a2320)}
.features svg.chev{position:absolute;top:0}
.feature h3{font-weight:400;font-size:16.5px;color:var(--cream);white-space:nowrap}
.feature p{font-size:10.8px;line-height:20px;color:#ddd;margin-top:6px;width:200px;padding-left:5px}
.feature-icon{border-radius:50%}

/* content panel */
.content{left:30px;top:545px;width:940px;height:497px;border-radius:8px;background:linear-gradient(#e4e4e4,#f4f4f4 55%,#fff)}
.welcome-title{left:48px;top:559px;font-size:22px;font-weight:400;color:var(--brand-red);white-space:nowrap}
.body-text{font-size:10.6px;line-height:20px;color:#333}
.btn-dark{background:linear-gradient(#5a5a5a,#1c1c1c);color:#cfcfcf;border-radius:5px;font-size:11px;text-align:center;line-height:20px}
.photo{border:3px solid #d6d6d6}
.more-link{color:var(--brand-red);font-size:13px}

.subpanel{left:36px;top:821px;width:632px;height:217px;border-radius:6px;background:linear-gradient(#c9c9c9,#e6e6e6 50%,#f7f7f7)}
.sub-title{font-size:14px;color:#222;text-decoration:underline;font-weight:400}
.thumb{border-radius:8px;border:2px solid #fff}
.pill{background:#0a0a0a;color:#fff;border-radius:8px;font-size:11px;line-height:16px;text-align:center}
.pill span{color:var(--brand-red)}

.side-box{border:1px solid var(--line);border-radius:8px;background:rgba(255,255,255,.6)}
.side-title{background:#f1f1f1;color:var(--brand-red);font-size:22px;padding:0 4px;white-space:nowrap;font-weight:400}
.side-list{font-size:10.4px}
.side-list li{list-style:none;position:relative;padding-left:23px;margin-bottom:20px}
.side-list li::before{content:"";position:absolute;left:6px;top:5px;width:8px;height:8px;border-radius:50%;background:#c4c4c4}
.side-list .date{position:absolute;right:0;bottom:0;color:var(--date)}

/* footer */
.footer-nav{top:1066px;left:51px;font-size:13px;color:#8a8a8a}
.footer-nav a{color:inherit;text-decoration:none;position:absolute;white-space:nowrap}
.copyright{left:700px;top:1057px;width:262px;text-align:right;font-size:10px;color:#8a8a8a;white-space:nowrap}
.footer-brand{left:600px;top:1120px;width:362px;text-align:right;font-weight:600;font-size:28px;color:#7a0d12;white-space:nowrap}
</style>
</head>
<body>

<header class="site-header abs">
  <div class="brand abs">Amber Tide Orbital</div>
  <div class="search abs">Search
    <svg width="22" height="20" viewBox="0 0 22 20"><circle cx="9" cy="8" r="6" fill="none" stroke="#b8b8b8" stroke-width="2.5"/><line x1="13" y1="12" x2="20" y2="18" stroke="#b8b8b8" stroke-width="3" stroke-linecap="round"/></svg>
  </div>
  <nav class="main-nav abs">
    <a class="current" href="#">Home</a>
    <a class="n2" href="#">Partners</a>
    <a class="n3" href="#">Jobs</a>
    <a class="n4" href="#">Contact us</a>
  </nav>
</header>

<section class="hero abs" role="img" aria-label="Night-time world map with city lights, a launching rocket and the Earth">
  <div class="hero-rocket abs"></div>
  <div class="hero-globe abs"></div>
  <p class="hero-tagline abs">Contrary to popular belief, Lorem Ipsum is not simply random text.</p>
</section>

<section class="features abs">
  <div class="first abs"></div>
  <svg class="chev" style="left:290px" width="70" height="96" viewBox="0 0 70 96"><polygon points="0,0 30,0 62,48 30,96 0,96 32,48" fill="#555" opacity=".6"/></svg>
  <svg class="chev" style="left:600px" width="70" height="96" viewBox="0 0 70 96"><polygon points="0,0 30,0 62,48 30,96 0,96 32,48" fill="#555" opacity=".6"/></svg>

  <div class="feature abs" style="left:6px;top:12px">
    <div class="feature-icon abs" role="img" aria-label="Ringed planet with moons" style="left:0;top:8px;width:64px;height:62px;background:radial-gradient(#d8d36a,#6a7a2a 60%,transparent 70%)"></div>
    <h3 class="abs" style="left:72px;top:-3px">Space Technology</h3>
    <p class="abs" style="left:73px;top:22px">Lorem Ipsum is simply dummy text of the printing and typesetting industry.</p>
  </div>
  <div class="feature abs" style="left:326px;top:12px">
    <div class="feature-icon abs" role="img" aria-label="Astronaut riding a small rocket" style="left:0;top:0;width:66px;height:80px;background:radial-gradient(#e8e8e8,#888 55%,transparent 70%)"></div>
    <h3 class="abs" style="left:70px;top:-3px">Robotic Rovers and Rockets</h3>
    <p class="abs" style="left:70px;top:27px">Lorem Ipsum is simply dummy text of the printing and typesetting industry.</p>
  </div>
  <div class="feature abs" style="left:656px;top:12px">
    <div class="feature-icon abs" role="img" aria-label="Cubesat with solar panels" style="left:0;top:0;width:70px;height:80px;background:radial-gradient(#5a7a5a,#2a3a2a 55%,transparent 70%)"></div>
    <h3 class="abs" style="left:81px;top:1px">Sats/Cubesats</h3>
    <p class="abs" style="left:78px;top:29px">Lorem Ipsum is simply dummy text of the printing and typesetting industry.</p>
  </div>
</section>

<main class="content abs"></main>
<h1 class="welcome-title abs">Welcome To Amber Tide Orbital</h1>
<p class="body-text abs" style="left:48px;top:592px;width:905px">There are many variations of passages of Lorem Ipsum available, but the majority have suffered alteration in some form, by injected humour, or randomised words which don't look even slightly believable. If you are going to use a passage of Lorem Ipsum, you need to be sure there isn't anything embarrassing hidden in the middle of text.</p>
<div class="btn-dark abs" style="left:820px;top:644px;width:98px;height:21px">Read more...</div>

<div class="photo abs" role="img" aria-label="Rocket launch at night on the pad" style="left:45px;top:666px;width:147px;height:131px;background:radial-gradient(circle at 35% 70%,#ffd27a,#a0501a 25%,#120c08 60%)"></div>
<p class="body-text abs" style="left:212px;top:663px;width:418px">There are many variations of passages of Lorem Ipsum available, but the majority have suffered alteration in some form, by injected humour, or randomised words which don't look even slightly believable. If you are going to use a passage of Lorem Ipsum, you need to be sure there isn't anything embarrassing hidden in the middle of text.</p>
<a class="more-link abs" style="left:573px;top:768px">more››</a>

<section class="subpanel abs"></section>
<h2 class="sub-title abs" style="left:158px;top:831px">Researchers</h2>
<h2 class="sub-title abs" style="left:418px;top:830px">Research Projects</h2>
<div class="thumb abs" role="img" aria-label="Astronaut in orbit beside a satellite above Earth" style="left:80px;top:857px;width:258px;height:113px;background:linear-gradient(120deg,#6a5a3a,#3a4a5a 50%,#c8c8c8)"></div>
<div class="thumb abs" role="img" aria-label="Engineer sketching a cubesat design" style="left:357px;top:857px;width:259px;height:113px;background:linear-gradient(90deg,#e8e8e8,#d8d8d8 50%,#c8a48a)"></div>
<p class="body-text abs" style="left:82px;top:972px;width:250px">There are many variations of passages of Lorem Ipsum available, but the majority have suffered alteration in some form,</p>
<p class="body-text abs" style="left:366px;top:970px;width:250px">There are many variations of passages of Lorem Ipsum available, but the majority have suffered alteration in some form,</p>
<div class="pill abs" style="left:245px;top:1018px;width:77px;height:17px"><span>more</span> details</div>
<div class="pill abs" style="left:525px;top:1012px;width:77px;height:17px"><span>more</span> details</div>

<aside class="side-box abs" style="left:679px;top:695px;width:278px;height:153px">
  <ul class="side-list body-text abs" style="left:0;top:22px;width:262px">
    <li>There are many variations of passages of Lorem Ipsum available,<span class="date">12/08/2011</span></li>
    <li>But the majority have suffered alteration in some form, by injected humour,<span class="date">18/12/2011</span></li>
  </ul>
</aside>
<h2 class="side-title abs" style="left:698px;top:680px">Conference/ Workshop</h2>

<aside class="side-box abs" style="left:679px;top:873px;width:279px;height:151px">
  <ul class="side-list body-text abs" style="left:0;top:22px;width:262px">
    <li>There are many variations of passages of Lorem Ipsum available,</li>
    <li>But the majority have suffered alteration in some form, by injected humour,</li>
  </ul>
</aside>
<h2 class="side-title abs" style="left:806px;top:857px">Latest News</h2>

<footer>
  <nav class="footer-nav abs">
    <a href="#" style="left:0">Home</a>
    <a href="#" style="left:105px">Partners</a>
    <a href="#" style="left:213px">Jobs</a>
    <a href="#" style="left:321px">Contact us</a>
  </nav>
  <p class="copyright abs">Copyright(c)2011 www.ambertide.example</p>
  <div class="footer-brand abs">Amber Tide Orbital</div>
</footer>

</body>
</html>
```